Brookvine Estates Business Card

Business Card:

Somewhere on front of card, please include Broker License Number: 5839261

Website is BrookvineEstates.com

Address is:
7216 Orchardpine Ave E
Saginaw, MI 48517

I'll let you use creative freedom on the rest; we obviously need Name, Title, Email (@BrookvineEstates.com), Office Phone, Cell Phone.

Don't want any special die-cutting, just a standard size business card.

On the back, include a place for the date and time of an appointment to be written in pen.

Industry/Entity Type

Business

Requirements
Must have
• Our logo, attached to email.

```html
<!DOCTYPE html>
<html lang="en">
<head>
<meta charset="utf-8">
<title>Brookvine Estates – Business Card</title>
<link rel="stylesheet" href="https://fonts.googleapis.com/css2?family=Arimo:wght@400;700&family=Roboto+Slab:wght@400;600&display=swap">
<style>
  :root {
    --panel-grey: #c3c4c7;
    --brand-navy: #2d2b88;
    --ink: #141414;
    --card-dark: #151515;
    --card-mid: #3a3a3a;
    --light-text: #ffffff;
  }
  * { margin: 0; padding: 0; box-sizing: border-box; }
  html, body { width: 1200px; height: 686px; overflow: hidden; background: #ffffff; }
  .card {
    position: relative;
    width: 1200px;
    height: 686px;
    overflow: hidden;
    font-family: "Arimo", Arial, sans-serif;
    background: radial-gradient(ellipse 60% 70% at 62% 45%, var(--card-mid) 0%, #222 55%, var(--card-dark) 100%);
  }
  .contact-panel {
    position: absolute;
    left: 0; top: 0;
    width: 434px; height: 686px;
    background: var(--panel-grey);
    overflow: hidden;
  }
  .person-name {
    position: absolute;
    left: 26px; top: 22px;
    font-size: 44px;
    line-height: 1;
    font-weight: 400;
    color: var(--ink);
    letter-spacing: -0.5px;
  }
  .person-name .surname { font-weight: 700; color: var(--brand-navy); }
  .person-title {
    position: absolute;
    left: 32px; top: 72px;
    font-size: 26px;
    color: var(--ink);
    letter-spacing: -0.5px;
  }
  .contact-list { position: absolute; left: 26px; top: 305px; width: 400px; list-style: none; }
  .contact-item {
    display: flex;
    align-items: center;
    height: 44px;
    margin-bottom: 14px;
    font-size: 21px;
    color: var(--ink);
    white-space: nowrap;
  }
  .contact-icon { width: 44px; height: 44px; margin-right: 10px; flex: none; }
  .skyline {
    position: absolute;
    left: 0; bottom: 0;
    width: 434px; height: 152px;
    background: linear-gradient(to top, var(--brand-navy) 0%, var(--brand-navy) 55%, rgba(45,43,136,0.55) 100%);
  }
  .license {
    position: absolute;
    right: 30px; top: 26px;
    font-family: "Roboto Slab", Georgia, serif;
    font-weight: 600;
    font-size: 17px;
    color: var(--light-text);
  }
  .brand-name {
    position: absolute;
    left: 434px; width: 766px;
    top: 300px;
    text-align: center;
    font-size: 64px;
    font-weight: 700;
    color: var(--brand-navy);
    letter-spacing: -0.5px;
  }
  .office-address {
    position: absolute;
    right: 26px; bottom: 26px;
    font-family: "Roboto Slab", Georgia, serif;
    font-size: 25px;
    color: var(--light-text);
    white-space: nowrap;
  }
</style>
</head>
<body>
<div class="card">
  <section class="contact-panel">
    <h1 class="person-name">DAN <span class="surname">MERCER</span></h1>
    <p class="person-title">Director</p>

    <ul class="contact-list">
      <li class="contact-item">
        <svg class="contact-icon" viewBox="0 0 44 44" aria-hidden="true">
          <circle cx="22" cy="22" r="19.5" fill="none" stroke="var(--brand-navy)" stroke-width="4"/>
          <path d="M15 12c1.5-1 3-.5 3.5.7l1.6 3.6c.4 1-.1 1.8-1 2.4l-1.2.8c.9 2.4 2.9 4.6 5.3 5.6l.9-1.1c.7-.9 1.6-1.2 2.5-.7l3.4 1.8c1.1.6 1.4 2 .5 3.3-1.4 2-3.5 2.7-6 1.8-5-1.8-9.4-6.4-10.8-11.5-.6-2.5.2-5 1.3-6.7z" fill="var(--ink)"/>
        </svg>
        <span>000-0000-0000</span>
      </li>
      <li class="contact-item">
        <svg class="contact-icon" viewBox="0 0 44 44" aria-hidden="true">
          <circle cx="22" cy="22" r="19.5" fill="none" stroke="var(--brand-navy)" stroke-width="4"/>
          <rect x="16" y="10" width="12" height="24" rx="2" fill="var(--ink)"/>
          <rect x="17.6" y="13" width="8.8" height="16" fill="var(--panel-grey)"/>
          <circle cx="22" cy="31.3" r="1.1" fill="var(--panel-grey)"/>
        </svg>
        <span>90000-00000</span>
      </li>
      <li class="contact-item">
        <svg class="contact-icon" viewBox="0 0 44 44" aria-hidden="true">
          <circle cx="22" cy="22" r="19.5" fill="none" stroke="var(--brand-navy)" stroke-width="4"/>
          <rect x="11" y="15" width="22" height="14" fill="var(--ink)"/>
          <path d="M12 16l10 7.5 10-7.5M12 28l7.5-6.5M32 28l-7.5-6.5" fill="none" stroke="var(--panel-grey)" stroke-width="1.4"/>
        </svg>
        <span>danmercer@BrookvineEstates.com</span>
      </li>
      <li class="contact-item">
        <svg class="contact-icon" viewBox="0 0 44 44" aria-hidden="true">
          <circle cx="22" cy="22" r="19.5" fill="none" stroke="var(--brand-navy)" stroke-width="4"/>
          <g fill="none" stroke="var(--ink)" stroke-width="1.6">
            <circle cx="22" cy="22" r="10"/>
            <ellipse cx="22" cy="22" rx="4.5" ry="10"/>
            <path d="M12 22h20M13.5 17h17M13.5 27h17"/>
          </g>
        </svg>
        <span>brookvineestates.com</span>
      </li>
    </ul>

    <div class="skyline" role="img" aria-label="City skyline silhouette in navy along the bottom of the panel"></div>
  </section>

  <p class="license">License No. :5839261</p>

  <h2 class="brand-name">Brookvine Estates</h2>

  <p class="office-address">#7216 Orchardpine Ave E,Saginaw, MI 48517</p>
</div>
</body>
</html>
```